Hair Salon Brochure

We need a brochure for our hair salon located in Middle Tennessee called Delphine Locks of Harbor Bend. Along with standard services, we offer specialized services and accommodations for individuals on the Autism Spectrum, regardless of background or hair type.
At Delphine Locks of Harbor Bend, our mission is to create a warm and inclusive haven for individuals of all backgrounds, including those on the autism spectrum and their families. We are dedicated to providing not only exceptional hairstyling services but also hands-on education and specialized cutting techniques for clients with natural textured hair. Our goal is to empower our clients with the knowledge and tools necessary to maintain a successful hair care routine, ensuring they leave our salon feeling confident.
We believe in fostering a sense of community, where parents of younger clients are encouraged to learn the proper hair care techniques for their children, promoting healthy practices at home. Our commitment extends beyond just hair; we are here to help you embrace your true self and recognize the beauty that resides within.
At Delphine Locks of Harbor Bend, our passion is to deliver the ultimate client experience, where you can be unapologetically yourself and feel completely at ease. From the moment you step through our doors, you are welcomed not only to discuss your hair concerns but also to engage in meaningful conversations about life. Together, we will collaborate on a personalized plan to achieve your hair goals and transform the way you perceive yourself.
Always remember, when you look good, you feel good, and when you feel good, you can achieve great things. We firmly believe that every individual is 'Beautiful Beyond the Spectrum,' and we are here to celebrate that beauty with you."
https://www.delphinelocks.net/
Tagline - "Beautiful Beyond the Spectrum"

```html
<!DOCTYPE html>
<html lang="en">
<head>
<meta charset="utf-8">
<title>Delphine Locks of Harbor Bend – Trifold Brochure</title>
<link href="https://fonts.googleapis.com/css2?family=Josefin+Sans:wght@400;600;700&family=Oswald:wght@700&family=Righteous&family=Kaushan+Script&display=swap" rel="stylesheet">
<style>
  :root{
    --blue:#0c5fb0;
    --blue-deep:#0a4f96;
    --orange:#dd6a25;
    --white:#ffffff;
    --ink:#1d1d1f;
    --page:#d9d9db;
  }
  *{margin:0;padding:0;box-sizing:border-box}
  html,body{width:803px;height:1200px;overflow:hidden;background:var(--page)}
  body{font-family:"Josefin Sans",sans-serif;color:var(--ink);position:relative}
  .spread{position:absolute;left:20px;width:763px;height:534px;background:var(--white);overflow:hidden;box-shadow:0 2px 6px rgba(0,0,0,.18)}
  .spread--outside{top:30px}
  .spread--inside{top:636px}
  .spread svg.shapes{position:absolute;inset:0;width:763px;height:534px}
  .copy{position:absolute;font-size:8.7px;line-height:1.22;font-weight:400}
  .copy p+p{margin-top:9px}
  .copy--light{color:var(--white)}
  .accent{color:var(--blue)}

  /* outside */
  .intro{left:34px;top:30px;width:190px}
  .logo-circle-name{position:absolute;left:640px;top:196px;width:96px;text-align:center;font-weight:600;font-size:12px;line-height:1.15;color:var(--blue)}
  .contact{position:absolute;left:300px;top:350px;width:230px;text-align:center}
  .contact__name{font-weight:600;font-size:17px;color:var(--blue);line-height:1.1}
  .contact__phone{font-family:"Oswald",sans-serif;font-weight:700;font-size:31px;color:var(--orange);margin-top:14px;letter-spacing:.5px}
  .contact__line{font-weight:700;font-size:14px;color:var(--blue);margin-top:4px}
  .tagline{position:absolute;left:540px;top:352px;width:220px;text-align:center}
  .tagline__main{font-family:"Righteous",sans-serif;font-size:34px;line-height:1;color:var(--blue)}
  .tagline__row{line-height:1;margin-top:2px}
  .tagline__sub{font-weight:600;font-size:18px;color:var(--orange);margin-right:4px}
  .tagline__script{font-family:"Kaushan Script",cursive;font-size:36px;color:var(--orange)}
  .web-band{position:absolute;right:16px;top:508px;font-weight:700;font-size:15px;line-height:1;color:var(--white)}

  /* inside */
  .mission{left:30px;top:26px;width:200px}
  .community{left:30px;top:252px;width:200px}
  .brand-mark{position:absolute;left:270px;top:80px;width:225px;text-align:center;font-weight:600;font-size:27px;line-height:1.1;color:var(--blue)}
  .passion{left:528px;top:26px;width:215px}
</style>
</head>
<body>

<section class="spread spread--outside" aria-label="Brochure outside">
  <svg class="shapes" viewBox="0 0 763 534">
    <defs>
      <linearGradient id="g-wash" x1="0" y1="0" x2="1" y2="1">
        <stop offset="0" stop-color="#4a4542"/><stop offset="1" stop-color="#1f1d1c"/>
      </linearGradient>
      <linearGradient id="g-salon" x1="0" y1="0" x2="1" y2="1">
        <stop offset="0" stop-color="#b9a79a"/><stop offset=".5" stop-color="#6d5c55"/><stop offset="1" stop-color="#2c2a2b"/>
      </linearGradient>
    </defs>
    <path class="band-blue" d="M0 0H300V200C250 165 190 118 0 108Z" fill="var(--blue)"/>
    <path class="photo-wash" role="img" aria-label="Photo: stylist washing a client's hair at a salon basin" d="M0 112C150 112 262 205 262 330C262 425 230 490 185 534H0Z" fill="url(#g-wash)"/>
    <path class="swoosh-orange" d="M238 0H300C272 60 266 130 286 215C252 150 236 80 238 0Z" fill="var(--orange)"/>
    <path class="arc-blue" d="M298 0C284 120 330 250 470 310C560 342 680 320 763 262" fill="none" stroke="var(--blue)" stroke-width="7"/>
    <path class="photo-stylists" role="img" aria-label="Photo: stylists cutting and styling clients' hair in the salon" d="M306 0H763V250C690 300 600 328 500 316C380 296 302 200 306 0Z" fill="url(#g-salon)"/>
    <path class="swoosh-orange" d="M470 332C590 350 700 325 763 286V298C700 340 600 360 470 340Z" fill="var(--orange)"/>
    <circle class="logo-circle" cx="688" cy="218" r="58" fill="var(--white)"/>
    <path class="band-blue" d="M360 534C470 520 640 505 763 440V534Z" fill="var(--blue)"/>
    <g class="contact-icons" transform="translate(382 495)">
      <circle cx="12" cy="12" r="11" fill="var(--blue)"/>
      <path d="M8 7.5l2-.5 1.4 3-1.2 1c.6 1.3 1.5 2.2 2.8 2.8l1-1.2 3 1.4-.5 2c-4.6.3-8.8-3.9-8.5-8.5z" fill="var(--white)"/>
      <circle cx="37" cy="12" r="11" fill="var(--blue)"/>
      <circle cx="37" cy="12" r="6" fill="none" stroke="var(--white)" stroke-width="1.3"/>
      <path d="M31 12h12M37 6c-3 3.5-3 8.5 0 12M37 6c3 3.5 3 8.5 0 12" fill="none" stroke="var(--white)" stroke-width="1.1"/>
      <circle cx="62" cy="12" r="11" fill="var(--blue)"/>
      <circle cx="62" cy="12" r="5" fill="none" stroke="var(--white)" stroke-width="1.4"/>
    </g>
  </svg>

  <div class="copy copy--light intro">Along with standard services, we offer specialized services and accommodations for individuals on the Autism Spectrum, regardless of background or hair type.</div>

  <div class="logo-circle-name">Delphine Locks<br>of Harbor Bend</div>

  <div class="contact">
    <div class="contact__name">Delphine Locks<br>of Harbor Bend</div>
    <div class="contact__phone">615-555-0142</div>
    <div class="contact__line">delphinelocks.net</div>
    <div class="contact__line">IG: @delphinelocksofhb</div>
  </div>

  <div class="tagline">
    <div class="tagline__main">Beautiful<br>Beyond</div>
    <div class="tagline__row"><span class="tagline__sub">the</span><span class="tagline__script">Spectrum</span></div>
  </div>

  <div class="web-band">www.delphinelocks.net</div>
</section>

<section class="spread spread--inside" aria-label="Brochure inside">
  <svg class="shapes" viewBox="0 0 763 534">
    <defs>
      <linearGradient id="g-tools" x1="0" y1="0" x2="1" y2="1">
        <stop offset="0" stop-color="#8d8d8d"/><stop offset="1" stop-color="#3b3b3b"/>
      </linearGradient>
      <linearGradient id="g-portrait" x1="0" y1="0" x2="0" y2="1">
        <stop offset="0" stop-color="#5a3a2c"/><stop offset=".45" stop-color="#2d2422"/><stop offset="1" stop-color="#161616"/>
      </linearGradient>
      <linearGradient id="g-interior" x1="0" y1="0" x2="1" y2="1">
        <stop offset="0" stop-color="#e6e6e6"/><stop offset="1" stop-color="#8e8e8e"/>
      </linearGradient>
    </defs>
    <path class="block-orange" d="M0 238H225Q255 238 255 268V534H0Z" fill="var(--orange)"/>
    <path class="photo-tools" role="img" aria-label="Photo: hair brushes, combs, scissors and styling products laid flat" d="M0 400C90 392 190 390 255 352V534H0Z" fill="url(#g-tools)"/>
    <path class="photo-portrait" role="img" aria-label="Photo: portrait of the salon owner smiling" d="M330 534V330C330 250 370 205 410 205C455 205 480 245 485 300C500 340 510 400 510 534Z" fill="url(#g-portrait)"/>
    <rect class="panel-blue" x="510" y="0" width="253" height="534" fill="var(--blue)"/>
    <path class="photo-interior" role="img" aria-label="Photo: modern salon interior with styling chairs and wash stations" d="M510 534V410C570 360 680 345 763 300V534Z" fill="url(#g-interior)"/>
    <circle class="photo-interior-detail" role="img" aria-label="Photo: salon mirrors and shelving" cx="594" cy="338" r="62" fill="#9fa3a6" stroke="var(--blue-deep)" stroke-width="6"/>
  </svg>

  <div class="copy mission">
    <p><span class="accent">At Delphine Locks of Harbor Bend, our mission is to create a warm and inclusive haven for individuals of all backgrounds</span>, including those on the autism spectrum and their families. We are dedicated to providing not only exceptional hairstyling services but also hands-on education and specialized cutting techniques for clients with natural textured hair.</p>
    <p>Our goal is to empower our clients with the knowledge and tools necessary to maintain a successful hair care routine, ensuring they leave our salon feeling confident.</p>
  </div>

  <div class="copy copy--light community">We believe in fostering a sense of community, where parents of younger clients are encouraged to learn the proper hair care techniques for their children, promoting healthy practices at home. Our commitment extends beyond just hair; we are here to help you embrace your true self and recognize the beauty that resides within.</div>

  <div class="brand-mark">Delphine Locks<br>of Harbor Bend</div>

  <div class="copy copy--light passion">
    <p>At Delphine Locks of Harbor Bend, our passion is to deliver the ultimate client experience, where you can be unapologetically yourself and feel completely at ease. From the moment you step through our doors, you are welcomed not only to discuss your hair concerns but also to engage in meaningful conversations about life. Together, we will collaborate on a personalized plan to achieve your hair goals and transform the way you perceive yourself.</p>
    <p>Always remember, when you look good, you feel good, and when you feel good, you can achieve great things. We firmly believe that every individual is 'Beautiful Beyond the Spectrum,' and we are here to celebrate that beauty with you."</p>
  </div>
</section>

</body>
</html>
```